Pest Control Company needs business card!

Hi there, we need a business card designed for our new Pest Control Company. Ideally this card will be simple, yet feel elegant and high end. We want to use the colours Orange, Black and White. Please see our attached logo for the exact colours.

Business card details:

Phone - 0438 517 264
Name - Gus Halloran
Email - Info@trueguardpest.com.au

We would also like to include the following list with dot points:

SERVICES / INSPECTIONS

Termites, Wood Borers, Ants, Cockroaches, Spiders, Fleas, Mice, Rats, Bed Bugs, & More!

```html
<!DOCTYPE html>
<html lang="en">
<head>
<meta charset="utf-8">
<title>TrueGuard Pest Control – Business Card</title>
<link rel="stylesheet" href="https://fonts.googleapis.com/css2?family=Montserrat:wght@600;700;800;900&display=swap">
<style>
  :root {
    --orange: #f47b20;
    --orange-deep: #c9600f;
    --black: #0b0b0b;
    --white: #ffffff;
    --page: #d9d9d9;
    --alert: #e3202a;
  }
  * { box-sizing: border-box; margin: 0; padding: 0; }
  html, body { width: 1200px; height: 900px; overflow: hidden; }
  body {
    background: var(--page);
    font-family: "Montserrat", sans-serif;
    position: relative;
  }
  .card {
    position: absolute;
    left: 250px;
    width: 700px;
    height: 400px;
    background: var(--black);
    overflow: hidden;
    box-shadow: 0 6px 18px rgba(0,0,0,.25);
  }
  .card--back { top: 35px; }
  .card--front { top: 465px; }

  /* back side */
  .services-tab {
    position: absolute;
    left: 0; top: 0;
    width: 420px; height: 52px;
    background: var(--orange);
    clip-path: polygon(0 0, 100% 0, 92% 100%, 0 100%);
    border-bottom-right-radius: 18px;
    color: var(--black);
    font-weight: 700;
    font-size: 19px;
    letter-spacing: 1px;
    display: flex; align-items: center;
    padding-left: 60px;
  }
  .more-tab {
    position: absolute;
    right: 0; bottom: 0;
    width: 230px; height: 50px;
    background: var(--orange);
    clip-path: polygon(10% 0, 100% 0, 100% 100%, 0 100%);
    color: var(--black);
    font-weight: 700;
    font-size: 17px;
    letter-spacing: 1px;
    display: flex; align-items: center; justify-content: center;
  }
  .pest {
    position: absolute;
    width: 110px;
    text-align: center;
  }
  .pest svg { display: block; margin: 0 auto; }
  .pest__label {
    margin-top: 6px;
    color: var(--white);
    font-weight: 700;
    font-size: 12px;
    letter-spacing: 1px;
  }

  /* front side */
  .brand {
    position: absolute;
    left: 150px; top: 95px;
    color: var(--orange);
    font-weight: 900;
    font-size: 46px;
    line-height: 1.02;
    letter-spacing: 1px;
  }
  .mascot {
    position: absolute;
    left: 470px; top: 40px;
    width: 150px; height: 160px;
    border-radius: 50%;
    background: var(--orange);
  }
  .phone-band {
    position: absolute;
    right: 0; top: 232px;
    width: 330px; height: 58px;
    background: var(--white);
    clip-path: polygon(6% 0, 100% 0, 100% 100%, 0 100%);
    display: flex; align-items: center;
    padding-left: 36px; gap: 12px;
  }
  .phone-band__number {
    color: var(--black);
    font-weight: 800;
    font-size: 32px;
    letter-spacing: 1px;
  }
  .email {
    position: absolute;
    right: 22px; top: 303px;
    color: var(--orange);
    font-weight: 700;
    font-size: 15px;
    letter-spacing: .5px;
    text-transform: uppercase;
  }
  .name-band {
    position: absolute;
    left: 0; bottom: 22px;
    width: 420px; height: 52px;
    background: var(--orange);
    clip-path: polygon(0 0, 100% 0, 95% 100%, 0 100%);
    display: flex; align-items: center;
    padding-left: 40px;
    color: var(--white);
    font-weight: 800;
    font-size: 26px;
    letter-spacing: 1.5px;
    text-transform: uppercase;
  }
</style>
</head>
<body>

<section class="card card--back" aria-label="Card back: services">
  <div class="services-tab">SERVICES / INSPECTIONS</div>

  <div class="pest" style="left:20px; top:95px;">
    <svg width="96" height="96" viewBox="0 0 96 96" role="img" aria-label="Termite icon">
      <g stroke="var(--orange)" stroke-width="2"><line x1="48" y1="2" x2="48" y2="14"/><line x1="48" y1="82" x2="48" y2="94"/><line x1="2" y1="48" x2="14" y2="48"/><line x1="82" y1="48" x2="94" y2="48"/></g>
      <circle cx="48" cy="48" r="36" fill="none" stroke="var(--orange)" stroke-width="2.5"/>
      <circle cx="48" cy="48" r="22" fill="var(--orange-deep)"/>
    </svg>
    <div class="pest__label">TERMITES</div>
  </div>
  <div class="pest" style="left:155px; top:95px;">
    <svg width="96" height="96" viewBox="0 0 96 96" role="img" aria-label="Wood borer beetle icon">
      <g stroke="var(--orange)" stroke-width="2"><line x1="48" y1="2" x2="48" y2="14"/><line x1="48" y1="82" x2="48" y2="94"/><line x1="2" y1="48" x2="14" y2="48"/><line x1="82" y1="48" x2="94" y2="48"/></g>
      <circle cx="48" cy="48" r="36" fill="none" stroke="var(--orange)" stroke-width="2.5"/>
      <circle cx="48" cy="48" r="22" fill="var(--orange-deep)"/>
    </svg>
    <div class="pest__label">WOOD BORERS</div>
  </div>
  <div class="pest" style="left:290px; top:95px;">
    <svg width="96" height="96" viewBox="0 0 96 96" role="img" aria-label="Ant icon">
      <g stroke="var(--orange)" stroke-width="2"><line x1="48" y1="2" x2="48" y2="14"/><line x1="48" y1="82" x2="48" y2="94"/><line x1="2" y1="48" x2="14" y2="48"/><line x1="82" y1="48" x2="94" y2="48"/></g>
      <circle cx="48" cy="48" r="36" fill="none" stroke="var(--orange)" stroke-width="2.5"/>
      <circle cx="48" cy="48" r="22" fill="var(--orange-deep)"/>
    </svg>
    <div class="pest__label">ANTS</div>
  </div>
  <div class="pest" style="left:425px; top:95px;">
    <svg width="96" height="96" viewBox="0 0 96 96" role="img" aria-label="Cockroach icon">
      <g stroke="var(--orange)" stroke-width="2"><line x1="48" y1="2" x2="48" y2="14"/><line x1="48" y1="82" x2="48" y2="94"/><line x1="2" y1="48" x2="14" y2="48"/><line x1="82" y1="48" x2="94" y2="48"/></g>
      <circle cx="48" cy="48" r="36" fill="none" stroke="var(--orange)" stroke-width="2.5"/>
      <circle cx="48" cy="48" r="22" fill="var(--orange-deep)"/>
    </svg>
    <div class="pest__label">COCKROACHES</div>
  </div>
  <div class="pest" style="left:565px; top:70px;">
    <svg width="96" height="96" viewBox="0 0 96 96" role="img" aria-label="Spider icon">
      <g stroke="var(--orange)" stroke-width="2"><line x1="48" y1="2" x2="48" y2="14"/><line x1="48" y1="82" x2="48" y2="94"/><line x1="2" y1="48" x2="14" y2="48"/><line x1="82" y1="48" x2="94" y2="48"/></g>
      <circle cx="48" cy="48" r="36" fill="none" stroke="var(--orange)" stroke-width="2.5"/>
      <circle cx="48" cy="48" r="22" fill="var(--orange-deep)"/>
    </svg>
    <div class="pest__label">SPIDERS</div>
  </div>

  <div class="pest" style="left:85px; top:225px;">
    <svg width="96" height="96" viewBox="0 0 96 96" role="img" aria-label="Flea icon">
      <g stroke="var(--orange)" stroke-width="2"><line x1="48" y1="2" x2="48" y2="14"/><line x1="48" y1="82" x2="48" y2="94"/><line x1="2" y1="48" x2="14" y2="48"/><line x1="82" y1="48" x2="94" y2="48"/></g>
      <circle cx="48" cy="48" r="36" fill="none" stroke="var(--orange)" stroke-width="2.5"/>
      <circle cx="48" cy="48" r="22" fill="var(--orange-deep)"/>
    </svg>
    <div class="pest__label">FLEAS</div>
  </div>
  <div class="pest" style="left:225px; top:225px;">
    <svg width="96" height="96" viewBox="0 0 96 96" role="img" aria-label="Mouse icon">
      <g stroke="var(--orange)" stroke-width="2"><line x1="48" y1="2" x2="48" y2="14"/><line x1="48" y1="82" x2="48" y2="94"/><line x1="2" y1="48" x2="14" y2="48"/><line x1="82" y1="48" x2="94" y2="48"/></g>
      <circle cx="48" cy="48" r="36" fill="none" stroke="var(--orange)" stroke-width="2.5"/>
      <circle cx="48" cy="48" r="22" fill="var(--orange-deep)"/>
    </svg>
    <div class="pest__label">MICE</div>
  </div>
  <div class="pest" style="left:365px; top:225px;">
    <svg width="96" height="96" viewBox="0 0 96 96" role="img" aria-label="Rat icon">
      <g stroke="var(--orange)" stroke-width="2"><line x1="48" y1="2" x2="48" y2="14"/><line x1="48" y1="82" x2="48" y2="94"/><line x1="2" y1="48" x2="14" y2="48"/><line x1="82" y1="48" x2="94" y2="48"/></g>
      <circle cx="48" cy="48" r="36" fill="none" stroke="var(--orange)" stroke-width="2.5"/>
      <circle cx="48" cy="48" r="22" fill="var(--orange-deep)"/>
    </svg>
    <div class="pest__label">RATS</div>
  </div>
  <div class="pest" style="left:505px; top:205px;">
    <svg width="96" height="96" viewBox="0 0 96 96" role="img" aria-label="Bed bug icon">
      <g stroke="var(--orange)" stroke-width="2"><line x1="48" y1="2" x2="48" y2="14"/><line x1="48" y1="82" x2="48" y2="94"/><line x1="2" y1="48" x2="14" y2="48"/><line x1="82" y1="48" x2="94" y2="48"/></g>
      <circle cx="48" cy="48" r="36" fill="none" stroke="var(--orange)" stroke-width="2.5"/>
      <circle cx="48" cy="48" r="22" fill="var(--orange-deep)"/>
    </svg>
    <div class="pest__label">BED BUGS</div>
  </div>

  <div class="more-tab">&amp; MORE!</div>
</section>

<section class="card card--front" aria-label="Card front: contact">
  <div class="brand">TRUEGUARD<br>PEST<br>CONTROL</div>
  <div class="mascot" role="img" aria-label="Cartoon bug mascot illustration"></div>

  <div class="phone-band">
    <svg width="26" height="26" viewBox="0 0 24 24" aria-hidden="true">
      <path fill="var(--alert)" d="M6.6 10.8a15.1 15.1 0 0 0 6.6 6.6l2.2-2.2a1 1 0 0 1 1-.25 11.4 11.4 0 0 0 3.6.57 1 1 0 0 1 1 1V20a1 1 0 0 1-1 1A17 17 0 0 1 3 4a1 1 0 0 1 1-1h3.5a1 1 0 0 1 1 1c0 1.25.2 2.45.57 3.57a1 1 0 0 1-.25 1z"/>
    </svg>
    <span class="phone-band__number">0438 517 264</span>
  </div>
  <div class="email">Info@trueguardpest.com.au</div>

  <div class="name-band">Gus Halloran</div>
</section>

</body>
</html>
```